Business Strategy Company
Cards & Paper for Enterprise Collaboration Data Company
Project: Business Strategy Company
Business Strategy Company -
Creative Brief
Professional
Tobin G. Maraselt
CEO
31927 Harrowgate Ave. Suite 400 Berkley, CA 90388
tobin@quandelrox.example
www.quandelrox.example
Please include tagline: "Connected Team Insight" We would like a clean, modern card like the types found in these designs: https://www.pendlewick.example/drafts/display/contest/93587/draft/705568 https://www.pendlewick.example/drafts/display/contest/79787/draft/600578 https://www.pendlewick.example/drafts/display/contest/77433/draft/650842 https://www.pendlewick.example/drafts/display/contest/50102/draft/406651 https://www.pendlewick.example/drafts/display/contest/101628/draft/769948 https://www.pendlewick.example/drafts/display/contest/101641/draft/771307 https://www.pendlewick.example/drafts/display/contest/99022/draft/771303
We like a field of dark color or a gradient with the logo in either white or a color just slightly lighter/darker than the background (i.e. if the background is black, the logo would either be white or very dark gray). We'd like to see both.

```html
<!DOCTYPE html>
<html lang="en">
<head>
<meta charset="utf-8">
<title>Quandelrox Stationery</title>
<link rel="stylesheet" href="https://fonts.googleapis.com/css2?family=Montserrat:wght@400;500;600&display=swap">
<style>
:root{
  --bg:#e8e5e0;
  --paper:#ffffff;
  --ink:#2b2b2b;
  --dark:#2a2a2c;
  --blue:#1ea2db;
  --grey:#7a7a7a;
  --rule:#c9c9c9;
}
*{box-sizing:border-box;margin:0;padding:0}
html,body{width:1200px;height:600px;overflow:hidden}
body{background:var(--bg);font-family:"Montserrat",sans-serif;color:var(--ink);position:relative}
.sheet{position:absolute;background:var(--paper);box-shadow:0 2px 6px rgba(0,0,0,.18);overflow:hidden}
.brand{display:flex;align-items:center;gap:6px;font-weight:500;color:var(--ink);white-space:nowrap}
.brand .mark{width:10px;height:10px;background:var(--blue);flex:none}
.brand.light{color:#fff}
.small{font-size:6px;line-height:1.5;color:var(--grey);white-space:nowrap}

/* letter-size sheets */
.letterhead,.fax{top:84px;width:336px;height:492px}
.letterhead{left:60px}
.fax{left:432px}
.sheet-brand{position:absolute;left:24px;top:24px;font-size:17px}
.head-address{position:absolute;left:160px;top:22px;padding-left:8px;border-left:1px solid var(--rule)}
.sheet-footer{position:absolute;left:0;right:0;bottom:18px;text-align:center}
.tagline{color:var(--blue);font-size:8px;font-weight:500;margin-bottom:4px;white-space:nowrap}
.sheet-footer .small{font-size:5.5px}

.fax-title{position:absolute;left:24px;top:100px;font-size:24px;font-weight:400;color:var(--blue);line-height:1}
.fax-table{position:absolute;left:24px;top:136px;width:288px}
.fax-row{display:flex;border-bottom:1px solid var(--rule);height:16px;align-items:flex-end;font-size:6px;color:var(--grey);padding-bottom:2px}
.fax-row span{flex:1}
.fax-checks{position:absolute;left:24px;top:218px;display:flex;gap:10px;font-size:5.5px;color:var(--grey);white-space:nowrap}
.fax-checks label{display:flex;align-items:center;gap:3px}
.fax-checks i{width:6px;height:6px;border:1px solid var(--grey);display:inline-block}

/* cards */
.card{top:108px;width:150px;height:80px}
.card-front{left:804px}
.card-back{left:966px;background:var(--dark)}
.card .brand{position:absolute;left:12px;top:12px;font-size:10px;gap:5px}
.card .brand .mark{width:8px;height:8px}
.card-person{position:absolute;left:12px;top:42px;font-size:5.5px;font-weight:600;white-space:nowrap}
.card-person em{display:block;font-style:normal;font-weight:400;color:var(--blue);font-size:5px}
.card-contact{position:absolute;left:82px;top:40px;font-size:4.3px}
.card-back .tagline{position:absolute;left:12px;bottom:12px;font-size:6px;color:#cfcfcf;margin:0}

/* envelopes */
.envelope{left:804px;width:341px;height:178px}
.env-front{top:204px}
.env-front .brand{position:absolute;left:16px;top:16px;font-size:13px}
.env-front .return{position:absolute;left:16px;top:38px;font-size:5px}
.recipient{position:absolute;left:196px;top:80px;width:122px}
.recipient div{border-bottom:1px solid var(--rule);height:12px}
.env-back{top:386px}
.env-back svg{position:absolute;left:0;top:0}
.env-back .tagline{position:absolute;left:0;right:0;top:34px;text-align:center;color:#d8d8d8;font-size:7px;margin:0}
</style>
</head>
<body>

<section class="sheet letterhead">
  <div class="brand sheet-brand"><span class="mark"></span>quandelrox</div>
  <div class="head-address small">31927 Harrowgate Ave. Suite 400<br>Berkley, CA 90388</div>
  <footer class="sheet-footer">
    <p class="tagline">Connected Team Insight</p>
    <p class="small">T 510.555.0186 &nbsp;|&nbsp; F 510.555.0187 &nbsp;|&nbsp; tobin@quandelrox.example &nbsp;|&nbsp; www.quandelrox.example</p>
  </footer>
</section>

<section class="sheet fax">
  <div class="brand sheet-brand"><span class="mark"></span>quandelrox</div>
  <div class="head-address small">31927 Harrowgate Ave. Suite 400<br>Berkley, CA 90388</div>
  <h1 class="fax-title">FAX</h1>
  <div class="fax-table">
    <div class="fax-row"><span>To:</span><span>From:</span></div>
    <div class="fax-row"><span>Fax:</span><span>Pages:</span></div>
    <div class="fax-row"><span>Phone:</span><span>Date:</span></div>
    <div class="fax-row"><span>Re:</span><span>CC:</span></div>
  </div>
  <div class="fax-checks">
    <label><i></i>Urgent</label>
    <label><i></i>For Review</label>
    <label><i></i>Please Comment</label>
    <label><i></i>Please Reply</label>
    <label><i></i>Please Recycle</label>
  </div>
  <footer class="sheet-footer">
    <p class="tagline">Connected Team Insight</p>
    <p class="small">T 510.555.0186 &nbsp;|&nbsp; F 510.555.0187 &nbsp;|&nbsp; tobin@quandelrox.example &nbsp;|&nbsp; www.quandelrox.example</p>
  </footer>
</section>

<section class="sheet card card-front">
  <div class="brand"><span class="mark"></span>quandelrox</div>
  <p class="card-person">Tobin G. Maraselt<em>CEO</em></p>
  <p class="card-contact small">T 510.555.0186<br>F 510.555.0187<br>M 510.555.0188<br>tobin@quandelrox.example<br>www.quandelrox.example</p>
</section>

<section class="sheet card card-back">
  <div class="brand light"><span class="mark"></span>quandelrox</div>
  <p class="tagline">Connected Team Insight</p>
</section>

<section class="sheet envelope env-front">
  <div class="brand"><span class="mark"></span>quandelrox</div>
  <p class="return small">31927 Harrowgate Ave. Suite 400<br>Berkley, CA 90388</p>
  <div class="recipient"><div></div><div></div><div></div><div></div></div>
</section>

<section class="sheet envelope env-back">
  <svg width="341" height="178" viewBox="0 0 341 178">
    <path d="M0 0 H341 V18 Q170 100 0 18 Z" fill="var(--dark)"/>
    <path d="M0 18 Q170 106 341 18" fill="none" stroke="var(--blue)" stroke-width="1"/>
  </svg>
  <p class="tagline">Connected Team Insight</p>
</section>

</body>
</html>
```